Fjellmark Botanics - Black Face Mask Packaging Design

We require packaging design for a charcoal activated blackhead removal peel off face mask (please see attachment of competitors product).

1: We require a logo for our brand name: 'Fjellmark Botanics'

2: We require a 3d rendered image of the box with the tube

3: We require label templates for both the box and the tube

The logo design brief is as follows:

We are bringing out a range of natural beauty products. We require a logo that represents norwegian natural beauty & incorporates the Norwegian Flag.

The packaging design brief is as follows:

Please attachment: (FBGen). There is an image of a woman with a black face mask.

1:We require our packaging design to have a generic face with a face mask being pulled off/stretched (as shown in the above attachment).
However, the face mask should display a Norwegian flag. The part of the mask that is still fixed to the face should be in full pastel Norwegian flag colors. The part of the mask that has been peeled away should be faded to charcoal grey (whilst maintaining the Norwegian flag). The ratio should be around 50/50 of mask attached to mask being peeled.
The colors throughout should be soft.

2:The design should also incorporate a unisex logo.(Please see attachment: FBUnisex)

3: The design should display the wording: 'Charcoal Activated Face Mask'

4: The design should also display the tagline: 'restores your youthful glow'

5: The back of the tube should display the ingredients: Please see attached. The back should also say ISO901 & GMPC certified

Please note, the packaging design for the tube should just be black and white as the printing machine on the tube can only be white.

The box can be a variation of colors as there are no restrictions on the colors for printing onto cardboard

Target Market(s)

Beauty, Natural Beauty, Unisex

Industry/Entity Type

Product

Logo Text

Fjellmark Botanics

Requirements
Must have
• Please refer to project description
Nice to have

```html
<!DOCTYPE html>
<html lang="en">
<head>
<meta charset="utf-8">
<title>Fjellmark Botanics – Charcoal Activated Face Mask Carton Dieline</title>
<link href="https://fonts.googleapis.com/css2?family=Josefin+Sans:wght@300;400&family=Roboto+Condensed:wght@400;700&display=swap" rel="stylesheet">
<style>
  :root {
    --backdrop-light: #f2f2f2;
    --backdrop-dark: #cfcfcf;
    --carton-black: #050607;
    --cut-line: #3a0d0f;
    --panel-grey: #2e2e2e;
    --label-taupe: #4a443e;
    --ink-white: #ffffff;
    --glow-red: #e3262b;
    --photo-light: #e9e9e9;
    --photo-mid: #9a8f88;
    --photo-skin: #c79a82;
  }
  * { margin: 0; padding: 0; box-sizing: border-box; }
  html, body { width: 1200px; height: 1200px; overflow: hidden; }
  body {
    background: radial-gradient(circle at 50% 45%, var(--backdrop-light) 0%, var(--backdrop-dark) 100%);
    font-family: "Roboto Condensed", sans-serif;
    color: var(--ink-white);
    position: relative;
  }
  .dieline { position: absolute; left: 0; top: 0; width: 1200px; height: 1200px; }
  .dieline .bleed { fill: var(--carton-black); stroke: var(--carton-black); stroke-width: 34; stroke-linejoin: round; }
  .dieline .cut { fill: none; stroke: var(--cut-line); stroke-width: 2; }

  .brand {
    position: absolute;
    display: flex; align-items: center; gap: 10px;
    font-family: "Josefin Sans", sans-serif; font-weight: 300;
    color: var(--ink-white); letter-spacing: 2px; line-height: 1.05;
    text-transform: uppercase; white-space: nowrap;
  }
  .brand-mark { width: 12px; height: 12px; background: var(--ink-white); flex: none; }

  .name-pill {
    position: absolute;
    background: var(--panel-grey);
    border-radius: 16px;
    font-family: "Josefin Sans", sans-serif; font-weight: 300;
    text-align: center; text-transform: uppercase; letter-spacing: 0.5px;
    line-height: 1.2; white-space: nowrap;
    display: flex; flex-direction: column; justify-content: center;
  }
  .info-box {
    position: absolute; left: 174px; width: 199px;
    background: var(--panel-grey); border-radius: 12px;
    padding: 8px 10px 8px 12px;
    text-transform: uppercase; font-size: 9px; line-height: 1.4;
  }
  .info-box h3 { font-size: 10.5px; font-weight: 700; margin-bottom: 6px; }
  .info-box p { margin-bottom: 9px; }
  .info-box p:last-child { margin-bottom: 0; }

  .origin {
    position: absolute; left: 174px; top: 855px;
    font-size: 10px; font-weight: 700; letter-spacing: 0.6px;
    display: flex; align-items: center; gap: 5px; white-space: nowrap;
  }
  .origin-square { width: 11px; height: 7px; background: var(--ink-white); }
  .volume { position: absolute; font-size: 14px; white-space: nowrap; }
  .volume small { font-size: 9px; }
  .volume.on-photo { color: var(--carton-black); }

  .front-label {
    position: absolute; left: 710px; top: 490px; width: 160px; height: 38px;
    background: var(--label-taupe);
    font-family: "Josefin Sans", sans-serif; font-weight: 300;
    font-size: 12px; letter-spacing: 0.3px; line-height: 1.3;
    padding: 4px 0 0 5px; text-transform: uppercase; white-space: nowrap;
    overflow: hidden;
  }
  .glow-badge {
    position: absolute; left: 795px; top: 512px; width: 75px; height: 36px;
    background: var(--ink-white); color: var(--glow-red);
    display: flex; align-items: center; gap: 4px; padding-left: 5px;
    text-transform: uppercase; font-weight: 700; line-height: 1; white-space: nowrap;
  }
  .glow-badge .unisex { width: 14px; height: 14px; border: 2px solid var(--carton-black); border-radius: 50%; flex: none; }
  .glow-badge .tag { display: flex; flex-direction: column; align-items: center; }
  .glow-badge .tag span:nth-child(1) { font-size: 7px; }
  .glow-badge .tag span:nth-child(2) { font-size: 4px; margin: 1px 0; }
  .glow-badge .tag span:nth-child(3) { font-size: 12px; letter-spacing: 0.5px; }

  .hero-photo {
    position: absolute; left: 630px; top: 550px; width: 240px; height: 334px;
    background:
      radial-gradient(ellipse at 45% 70%, var(--photo-skin) 0%, rgba(199,154,130,0) 55%),
      linear-gradient(180deg, var(--carton-black) 0%, var(--photo-light) 22%, var(--photo-mid) 60%, var(--photo-skin) 100%);
  }
</style>
</head>
<body>

<svg class="dieline" viewBox="0 0 1500 1500" aria-hidden="true">
  <g class="bleed">
    <path d="M190 395 L190 100 Q190 40 240 35 L440 35 Q490 40 490 100 L490 395 Z"/>
    <path d="M190 400 L118 415 L118 1085 L190 1105 Z"/>
    <path d="M490 395 L490 215 L745 215 L790 380 L790 395 Z"/>
    <path d="M1088 395 L1088 380 L1130 215 L1355 215 L1385 395 Z"/>
    <rect x="190" y="395" width="1195" height="710"/>
    <rect x="787" y="380" width="301" height="30"/>
    <path d="M490 1105 L490 1120 L540 1285 L755 1285 L790 1120 L790 1105 Z"/>
    <path d="M1088 1105 L1105 1120 L1140 1285 L1335 1285 L1385 1105 Z"/>
    <path d="M790 1105 L790 1390 Q795 1460 850 1465 L1030 1465 Q1088 1460 1088 1390 L1088 1105 Z"/>
  </g>
  <g class="cut">
    <path d="M190 395 L190 100 Q190 40 240 35 L440 35 Q490 40 490 100 L490 395"/>
    <path d="M190 400 L118 415 L118 1085 L190 1105"/>
    <path d="M490 395 L490 215 L745 215 L790 380"/>
    <path d="M1088 380 L1130 215 L1355 215 L1385 395"/>
    <path d="M190 395 L1385 395 M190 1105 L1385 1105 M190 395 L190 1105 M490 395 L490 1105 M790 395 L790 1105 M1088 395 L1088 1105 M1385 395 L1385 1105"/>
    <path d="M490 1105 L540 1285 L755 1285 L790 1120"/>
    <path d="M1105 1120 L1140 1285 L1335 1285 L1385 1105"/>
    <path d="M790 1105 L790 1390 Q795 1460 850 1465 L1030 1465 Q1088 1460 1088 1390 L1088 1105"/>
  </g>
</svg>

<!-- Top tuck flap -->
<div class="brand" style="left:175px; top:140px; font-size:19px;"><span class="brand-mark"></span><span>Fjellmark<br>Botanics</span></div>
<div class="name-pill" style="left:193px; top:259px; width:160px; height:34px; font-size:10.5px;">
  <span>Charcoal Activated</span><span>Face Mask</span>
</div>

<!-- Back panel -->
<div class="brand" style="left:172px; top:375px; font-size:23px;"><span class="brand-mark"></span><span>Fjellmark<br>Botanics</span></div>
<div class="name-pill" style="left:174px; top:531px; width:199px; height:42px; font-size:13px;">
  <span>Charcoal Activated</span><span>Face Mask</span>
</div>
<div class="info-box" style="top:590px; height:116px;">
  <h3>How to:</h3>
  <p>1. Apply a thin even layer to clean dry skin, avoiding eye area.</p>
  <p>2. Leave mask on skin about 10 minutes, or until dry and rinse well.</p>
  <p>3. Use 1-2 times a week or as needed.</p>
</div>
<div class="info-box" style="top:726px; height:114px;">
  <h3>Ingredients:</h3>
  <p>Water, butylene gycol , cellulose gun, glycerin, charcoal powder, retinyl palmite, lecithin, calendula officinalis , flower extract , citrus gradis, grapefruit fruit extract, rosemary leaf extract.</p>
</div>
<div class="origin"><span class="origin-square"></span>MADE IN NORWAY</div>
<div class="volume" style="left:337px; top:852px;">50 <small>ML</small></div>

<!-- Front panel -->
<div class="brand" style="left:655px; top:372px; font-size:23px;"><span class="brand-mark"></span><span>Fjellmark<br>Botanics</span></div>
<div class="front-label">Charcoal Activated<br>Face Mask</div>
<div class="glow-badge">
  <span class="unisex"></span>
  <span class="tag"><span>Restores</span><span>Your youthful</span><span>Glow</span></span>
</div>
<div class="hero-photo" role="img" aria-label="Photo of a model peeling off a charcoal face mask painted with the Norwegian flag, against a white powder splash"></div>
<div class="volume on-photo" style="left:831px; top:865px;">50 <small>ML</small></div>

</body>
</html>
```